Palvanor Lending. Website design for a mortgage company.

We need a simple, but classy and artistic website design. The website should contain a home page, about page, and information page. I would like the design for each page created and I can add the content.

Palvanor Lending is a retail mortgage broker business specially crafted to provide simple, transparent, and comprehensive mortgage solutions. We understand the complexities of mortgage acquisition and have aligned with the best partners and resources to analyze the information and deliver precise, transparent, efficient, and reliable results.

Target Market(s)

We are targeting people ages 30-65 within the United States, both male and female. We are also targeting business owners and property investors specifically.

Industry/Entity Type

Mortgage Brokerage

Coding

Coded - Design and coding required

Number of Pages Required

5+ page

Font styles to use
Sans Serif
Script

Requirements
Must have
• The main purpose of this website is to provide clients with the necessary information to want to move forward with a loan transaction. The website will be informational to promote the company and showcase our purpose. The company purpose is to provide efficient and comprehensive service to clients, and to help them navigate the challenging mortgage world.

The website must mimic that of the major fortune 500 companies. It needs to be super clean, but very modern. The pictures should be of families with brown skin mostly.

The website needs to be mobile responsive. Each page needs to consist of large and responsive Hero Images. There will be background videos on the product and process pages of the website.

The website must have a semi-flat design.
The website must have a Hamburger Menu instead of a visible navigation menu.

Use the script font styles for the headlines and the sans serif for body text.

We need to have the following pages:
Home

Products

Process

About

Contact - I want a map of our office location and region. We are located in Bowie MD and our region consists of the following states: Florida, Texas, Virginia, Maryland, and Washington DC.

```html
<!DOCTYPE html>
<html lang="en">
<head>
<meta charset="utf-8">
<title>Palvanor Lending</title>
<link href="https://fonts.googleapis.com/css2?family=Montserrat:wght@500;600;700&family=Arimo:wght@400;700&display=swap" rel="stylesheet">
<style>
:root{
  --green:#1db155;
  --green-dark:#179a48;
  --ink:#2b2b2b;
  --muted:#666;
  --line:#e2e2e2;
  --footer:#2b2b2d;
  --white:#fff;
}
*{box-sizing:border-box;margin:0;padding:0}
html,body{width:1200px;height:3579px;overflow:hidden}
body{font-family:"Arimo",Arial,sans-serif;color:var(--muted);background:var(--white);position:relative}
section,header,footer{position:absolute;left:0;width:1200px}
.abs{position:absolute}
.heading{font-family:"Montserrat",Arial,sans-serif;font-weight:700;text-transform:uppercase;color:var(--ink)}
.heading .accent{color:var(--green)}
.center{text-align:center;left:0;width:1200px}

/* header */
.site-header{top:0;height:113px;background:var(--white);z-index:3}
.brand{position:absolute;left:109px;top:-10px;width:208px;height:208px;border-radius:50%;background:var(--white);text-align:center;padding-top:110px}
.brand-dot{width:34px;height:34px;border-radius:50%;background:var(--green);margin:0 auto 10px;position:absolute;left:87px;top:52px}
.brand-name{font-family:"Montserrat",sans-serif;font-weight:700;font-size:16px;color:var(--ink);letter-spacing:.2px}
.brand-tag{font-family:"Montserrat",sans-serif;font-weight:600;font-size:11px;color:var(--green);margin-top:2px}
.menu-btn{position:absolute;left:1032px;top:34px;width:56px;height:56px;border-radius:50%;border:2px solid var(--green)}
.menu-btn span{position:absolute;left:19px;width:16px;height:3px;background:var(--ink)}

/* hero */
.hero{top:113px;height:705px;background:linear-gradient(180deg,#3b4148 0%,#2f3a33 45%,#2d3b22 75%,#26301c 100%);z-index:1}
.hero-title{top:300px;font-size:58px;color:var(--white);letter-spacing:.5px}
.hero-sub{top:382px;font-family:"Montserrat",sans-serif;font-weight:500;font-size:21px;line-height:35px;color:var(--white);text-transform:uppercase}
.play{left:562px;top:467px;width:76px;height:76px;border-radius:50%;border:3px solid var(--white)}

/* products */
.products{top:818px;height:506px}
.sec-title{font-size:33px}
.sec-sub{font-size:14.5px;color:#555}
.product{position:absolute;width:270px;text-align:center}
.product-icon{width:138px;height:138px;border-radius:50%;background:var(--green);margin:0 auto;position:relative;border:4px solid var(--green)}
.product-icon::after{content:"";position:absolute;inset:5px;border-radius:50%;border:3px solid var(--white)}
.product-icon svg{position:absolute;left:34px;top:34px}
.product h3{font-family:"Montserrat",sans-serif;font-weight:600;font-size:18px;color:var(--ink);margin-top:21px;text-transform:uppercase}
.product p{font-size:14.5px;line-height:28px;margin-top:12px;color:#666}

/* about */
.about{top:1324px;height:547px;background:linear-gradient(90deg,#f3f6fa 0%,#eef2f6 60%,#e7ebf0 100%)}
.about-art{left:600px;top:0;width:600px;height:547px;background:linear-gradient(160deg,#eef1f5 0%,#dde3ea 50%,#c9bfb2 88%,#b88f68 100%)}
.about-floor{left:0;top:522px;width:600px;height:25px;background:linear-gradient(180deg,#d8b690,#b88f68)}
.about h2{left:111px;top:80px;font-size:33px}
.about p{left:111px;top:152px;width:485px;font-size:14px;line-height:28.2px;color:#555}
.btn{left:111px;top:347px;width:154px;height:51px;background:var(--green);color:var(--white);font-family:"Montserrat",sans-serif;font-weight:500;font-size:16px;line-height:51px;text-align:center;border-radius:2px}

/* process */
.process{top:1871px;height:457px;background:linear-gradient(180deg,#1eb257,#1aa94f)}
.process .sec-title{color:var(--white)}
.process .sec-sub{color:var(--white)}
.step{position:absolute;top:156px;width:235px;height:250px;background:var(--white);text-align:center}
.step svg{margin-top:28px}
.step h3{font-family:"Montserrat",sans-serif;font-weight:600;font-size:15px;color:var(--ink);margin-top:14px}
.step p{font-size:13.5px;line-height:23px;margin-top:13px;color:#666;padding:0 14px}

/* news */
.news{top:2328px;height:585px}
.news .sec-title{color:var(--green)}
.card{position:absolute;top:164px;width:467px;height:363px;border:1px solid var(--line);background:var(--white)}
.card-img{position:relative;height:221px}
.card-img.family{background:linear-gradient(135deg,#8d8a82 0%,#5d5348 45%,#3c3a35 100%)}
.card-img.house{background:linear-gradient(180deg,#2f5b9a 0%,#1f3c6a 50%,#3a3526 100%)}
.date{position:absolute;left:0;bottom:0;height:40px;width:154px;background:var(--green);color:var(--white);font-family:"Montserrat",sans-serif;font-weight:500;font-size:13px;line-height:40px;padding-left:17px;clip-path:polygon(0 0,86% 0,100% 100%,0 100%)}
.card h3{font-family:"Montserrat",sans-serif;font-weight:600;font-size:17px;color:var(--ink);margin:30px 0 0 22px}
.card p{font-size:13.5px;line-height:25px;margin:13px 20px 0 22px;color:#666}
.card p a{color:var(--green);text-decoration:none}

/* map */
.map{top:2913px;height:351px;background:linear-gradient(100deg,#eef0e4 0%,#e4ead9 35%,#cfe3c2 70%,#d8e6f1 88%,#a9cbe8 100%)}

/* footer */
.site-footer{top:3264px;height:315px;background:var(--footer);color:#ccc}
.contact{position:absolute;top:30px;width:300px;text-align:center}
.contact-icon{width:66px;height:66px;border-radius:50%;border:2px solid #8a8a8a;margin:0 auto;position:relative}
.contact-icon svg{position:absolute;left:21px;top:21px}
.contact h4{font-family:"Montserrat",sans-serif;font-weight:500;font-size:17px;color:var(--white);margin-top:17px;letter-spacing:.3px}
.contact p{font-size:12.5px;line-height:23px;margin-top:6px;color:#c9c9c9}
.divider{left:111px;top:230px;width:978px;height:1px;background:#3d3d40}
.copy{left:111px;top:262px;font-size:13px;color:#e6e6e6}
.social{top:253px;left:879px;display:flex;gap:8px}
.social span{width:35px;height:35px;border-radius:50%;border:2px solid #dcdcdc;display:block}
</style>
</head>
<body>

<header class="site-header">
  <div class="brand">
    <div class="brand-dot"></div>
    <div class="brand-name">PALVANOR LENDING</div>
    <div class="brand-tag">A Retail Mortgage Broker</div>
  </div>
  <div class="menu-btn" aria-label="Menu">
    <span style="top:19px"></span><span style="top:25px"></span><span style="top:31px"></span>
  </div>
</header>

<section class="hero" role="img" aria-label="Large brick family home with a green lawn at dusk">
  <h1 class="abs center heading hero-title">Palvanor Lending</h1>
  <p class="abs center hero-sub">Palvanor Lending is a retail mortgage broker business specially<br>crafted to provide simple, transparent</p>
  <div class="abs play">
    <svg width="70" height="70" viewBox="0 0 70 70"><path d="M29 23 L49 35 L29 47 Z" fill="#fff"/></svg>
  </div>
</section>

<section class="products">
  <h2 class="abs center heading sec-title" style="top:48px">Our <span class="accent">Products</span></h2>
  <p class="abs center sec-sub" style="top:108px">Sed ut perspiciatis unde omnis iste natus error sit voluptatem accusantium doloremque laudantium</p>

  <div class="product" style="left:136px;top:169px">
    <div class="product-icon">
      <svg width="70" height="70" viewBox="0 0 70 70" fill="#fff"><path d="M8 30 Q35 0 62 30 Z"/><rect x="34" y="28" width="2.5" height="14"/><rect x="12" y="44" width="46" height="14" rx="5"/><path d="M18 44 L24 36 H46 L52 44 Z"/><circle cx="21" cy="59" r="4" fill="#1db155"/><circle cx="49" cy="59" r="4" fill="#1db155"/></svg>
    </div>
    <h3>Auto Insurance</h3>
    <p>Sed ut perspiciatis unde omnis iste natus error sit voluptatem accusantium mque laudantium totam</p>
  </div>

  <div class="product" style="left:468px;top:169px">
    <div class="product-icon">
      <svg width="70" height="70" viewBox="0 0 70 70" fill="#fff"><circle cx="22" cy="12" r="8"/><path d="M10 24 H34 V44 H28 V66 H16 V44 H10 Z"/><path d="M38 30 L54 24 L68 30 V46 Q68 60 54 66 Q40 60 38 46 Z"/><text x="53" y="53" font-family="Arimo,sans-serif" font-weight="700" font-size="18" fill="#1db155" text-anchor="middle">$</text></svg>
    </div>
    <h3>Business Insurance</h3>
    <p>Sed ut perspiciatis unde omnis iste natus error sit voluptatem accusantium mque laudantium totam</p>
  </div>

  <div class="product" style="left:801px;top:169px">
    <div class="product-icon">
      <svg width="70" height="70" viewBox="0 0 70 70" fill="none" stroke="#fff" stroke-width="4"><path d="M20 30 L38 14 L56 30 V44 H20 Z"/><rect x="33" y="32" width="9" height="10" fill="#fff"/><path d="M6 52 Q20 46 34 52 H50 Q58 50 64 44" stroke-linecap="round"/><path d="M6 60 H44 Q56 58 66 50" stroke-linecap="round"/></svg>
    </div>
    <h3>Home Insurance</h3>
    <p>Sed ut perspiciatis unde omnis iste natus error sit voluptatem accusantium mque laudantium totam</p>
  </div>
</section>

<section class="about">
  <div class="abs about-floor"></div>
  <div class="abs about-art" role="img" aria-label="Young couple sitting on a wooden floor looking up at sketched lamps, a picture frame and shelves on a white wall"></div>
  <h2 class="abs heading">About <span class="accent">Us</span></h2>
  <p class="abs">Sed ut perspiciatis unde omnis iste natus error sit voluptatem accusantium do loremque laudantium, totam rem aperiam, eaque ipsa quae ab illo inventore veritatis et quasi architecto beatae vitae dicta sunt explicabo. Nemo enim ipsam voluptatem quia voluptas sit aspernatur aut odit aut fugit, sed quia consequuntur magni dolores eos qui ratione voluptatem sequi nesciunt.</p>
  <a class="abs btn">READ MORE</a>
</section>

<section class="process">
  <h2 class="abs center heading sec-title" style="top:48px">Our Process</h2>
  <p class="abs center sec-sub" style="top:103px">Sed ut perspiciatis unde omnis iste natus error sit voluptatem accusantium doloremque laudantium</p>

  <div class="step" style="left:111px">
    <svg width="82" height="72" viewBox="0 0 82 72" fill="none" stroke="#333" stroke-width="3" stroke-linecap="round"><path d="M58 20 A30 30 0 1 0 58 52"/><path d="M34 16 V36 H20"/><path d="M56 28 L64 36 L56 44"/><path d="M66 28 L74 36 L66 44"/></svg>
    <h3>QUICK DEALS</h3>
    <p>Sed ut perspiciatis unde omnis iste natus error sit voluptatem accusantium doloremque</p>
  </div>
  <div class="step" style="left:359px">
    <svg width="82" height="72" viewBox="0 0 82 72" fill="none" stroke="#333" stroke-width="3" stroke-linejoin="round"><path d="M36 4 L52 12 V30 L36 38 L20 30 V12 Z"/><path d="M20 12 L36 20 L52 12 M36 20 V38"/><rect x="6" y="48" width="8" height="18"/><path d="M14 52 H30 Q38 52 42 58 H56 L70 48 Q76 48 72 56 L58 66 H14"/></svg>
    <h3>EXCLUSIVE OFFERS</h3>
    <p>Sed ut perspiciatis unde omnis iste natus error sit voluptatem accusantium doloremque</p>
  </div>
  <div class="step" style="left:606px">
    <svg width="82" height="72" viewBox="0 0 82 72" fill="none" stroke="#333" stroke-width="3" stroke-linecap="round" stroke-linejoin="round"><path d="M28 70 V54 Q16 46 16 30 Q16 6 40 6 Q62 6 62 28 L68 40 H62 V50 Q62 56 54 56 H48 V70"/><path d="M32 34 Q26 34 26 28 Q26 22 32 22 Q34 16 40 16 Q48 16 48 24 Q54 24 54 30 Q54 34 48 34 Z"/><path d="M40 44 V30 M36 34 L40 30 L44 34"/></svg>
    <h3>EXPERIENCE</h3>
    <p>Sed ut perspiciatis unde omnis iste natus error sit voluptatem accusantium doloremque</p>
  </div>
  <div class="step" style="left:854px">
    <svg width="82" height="72" viewBox="0 0 82 72" fill="none" stroke="#333" stroke-width="3.5" stroke-linecap="round" stroke-linejoin="round"><circle cx="41" cy="36" r="32"/><path d="M27 37 L37 47 L56 26"/></svg>
    <h3>HAPPY CLIENTS</h3>
    <p>Sed ut perspiciatis unde omnis iste natus error sit voluptatem accusantium doloremque</p>
  </div>
</section>

<section class="news">
  <h2 class="abs center heading sec-title" style="top:60px">Latest News</h2>
  <p class="abs center sec-sub" style="top:116px">Sed ut perspiciatis unde omnis iste natus error sit voluptatem accusantium doloremque laudantium</p>

  <article class="card" style="left:112px">
    <div class="card-img family" role="img" aria-label="Father and daughter washing dishes together at a kitchen sink">
      <div class="date">02 MARCH 2020</div>
    </div>
    <h3>SED UT PERSPICIATIS UNDE OMNIS</h3>
    <p>Nemo enim ipsam voluptatem quia voluptas sit aspernatur aut odit aut eos qui ratione voluptatem sequi nesciunt. <a>READ MORE</a></p>
  </article>

  <article class="card" style="left:618px">
    <div class="card-img house" role="img" aria-label="Modern glass-fronted house lit up at twilight">
      <div class="date">02 MARCH 2020</div>
    </div>
    <h3>SED UT PERSPICIATIS UNDE OMNIS</h3>
    <p>Nemo enim ipsam voluptatem quia voluptas sit aspernatur aut odit aut eos qui ratione voluptatem sequi nesciunt. <a>READ MORE</a></p>
  </article>
</section>

<section class="map" role="img" aria-label="Road map of the eastern United States with a red location pin in Maryland"></section>

<footer class="site-footer">
  <div class="contact" style="left:117px">
    <div class="contact-icon"><svg width="22" height="22" viewBox="0 0 22 22"><path d="M11 1 Q4 1 4 8 Q4 13 11 21 Q18 13 18 8 Q18 1 11 1 Z" fill="#fff"/><circle cx="11" cy="8" r="3" fill="#2b2b2d"/></svg></div>
    <h4>LOCATION</h4>
    <p>#245 Lorem Ipsum Dummy text<br>Lorem Ipsum DUmmy</p>
  </div>
  <div class="contact" style="left:450px">
    <div class="contact-icon"><svg width="22" height="22" viewBox="0 0 22 22"><path d="M5 2 L9 2 L10 7 L7 9 Q9 13 13 15 L15 12 L20 13 L20 17 Q20 20 17 20 Q3 19 2 5 Q2 2 5 2 Z" fill="#fff"/></svg></div>
    <h4>CONTACT</h4>
    <p>Office: 000-121-1231<br>Fax: 000-121-1231</p>
  </div>
  <div class="contact" style="left:781px">
    <div class="contact-icon"><svg width="22" height="22" viewBox="0 0 22 22"><rect x="2" y="5" width="18" height="13" rx="1.5" fill="#fff"/><path d="M2 6 L11 13 L20 6" stroke="#2b2b2d" stroke-width="1.6" fill="none"/></svg></div>
    <h4>EMAIL</h4>
    <p>info@palvanorlending.com<br>www.palvanorlending.com</p>
  </div>
  <div class="abs divider"></div>
  <p class="abs copy">© Copyright 2020 Palvanor Lending.All rights reserved.</p>
  <div class="abs social" aria-label="Social links">
    <span></span><span></span><span></span><span></span><span></span>
  </div>
</footer>

</body>
</html>
```